Design for a Service-Based Estimate

We want a design for an Estimate that will always be sent in PDF format. The estimate or proposal is a critical document that needs to plainly show the service items, item description but also needs to be attractive and professional looking. Our current estimate deliverable is attached but it looks really basic like a Word document

```html
<!DOCTYPE html>
<html lang="en">
<head>
<meta charset="utf-8">
<title>Estimate – Keystone Paving</title>
<link href="https://fonts.googleapis.com/css2?family=Fira+Sans:wght@500;600;700&family=Open+Sans:wght@400;600;700&display=swap" rel="stylesheet">
<style>
:root{
  --navy:#27234f;
  --orange:#d04122;
  --grey:#808080;
  --stage:#595758;
  --ink:#1f1f1f;
  --rule:#8a8a8a;
  --paper:#ffffff;
  --faint:#cbc6d6;
}
*{margin:0;padding:0;box-sizing:border-box}
html,body{width:1200px;height:1200px;overflow:hidden;background:var(--stage)}
body{position:relative;font-family:'Open Sans',sans-serif;color:var(--ink)}
.page{position:absolute;top:212px;width:531px;height:751px;background:var(--paper);overflow:hidden}
.page--estimate{left:48px}
.page--terms{left:621px}
.header-art{position:absolute;left:0;top:0}
.brand{position:absolute;font-family:'Fira Sans',sans-serif;font-weight:700;letter-spacing:1px;white-space:nowrap}
.brand--header{left:12px;top:24px;font-size:22px;color:#fff}
.brand--footer{left:323px;top:675px;font-size:20px;color:var(--navy)}
.brand--faint{left:0;width:531px;text-align:center;top:592px;font-size:46px;color:var(--faint);letter-spacing:2px}
.recipient{position:absolute;left:282px;top:17px;color:#fff;font-size:16px;line-height:21.5px;white-space:nowrap}
.recipient strong{font-family:'Fira Sans',sans-serif;font-weight:600}
.estimate-title{position:absolute;left:0;width:531px;top:113px;text-align:center}
.estimate-title h1{font-family:'Fira Sans',sans-serif;font-weight:600;font-size:31px;line-height:34px;color:var(--navy);letter-spacing:.5px}
.estimate-title h2{font-family:'Fira Sans',sans-serif;font-weight:500;font-size:21px;line-height:22px;color:#000}
.estimate-title p{font-size:14px;line-height:22px;color:#222}
.line-items{position:absolute;left:12px;top:209px;width:501px;border-collapse:collapse;table-layout:fixed}
.line-items th{background:var(--orange);color:#fff;font-family:'Fira Sans',sans-serif;font-weight:600;font-size:15px;height:47px;text-align:left;padding:0 8px;border-right:1px solid #e6a090}
.line-items th:last-child{border-right:none}
.line-items th.c{text-align:center}
.line-items td{border:1px solid var(--rule);font-size:10px;line-height:13.6px;vertical-align:top;padding:14px 4px 0}
.line-items td.desc{padding:14px 12px 0 13px}
.line-items td.num{text-align:center;font-size:10.5px}
.line-items td.money{text-align:right;font-size:10.5px;padding-right:2px}
.line-items tr.row-main td{height:100px}
.line-items tr.row-opt td{height:46px;padding-top:14px}
.line-items tr.row-total td{height:46px;padding-top:16px;font-weight:700}
.line-items tr.row-total td.label{text-align:right;padding-right:15px;font-size:10.5px}
.line-items tr:first-child td,.line-items tr.row-opt td,.line-items tr.row-total td{border-top-color:#333}
.foot-band{position:absolute;left:0;bottom:0;width:531px;height:16px;background:var(--navy)}
.terms-title{position:absolute;left:0;width:531px;top:49px;text-align:center;font-family:'Fira Sans',sans-serif;font-weight:600;font-size:22px;color:var(--navy);letter-spacing:.4px}
.dotted{position:absolute;left:12px;width:500px;border-top:2px dotted var(--orange)}
.terms-list{list-style:none}
.terms-list li{position:absolute;left:59px;width:456px;font-size:10px;line-height:13.6px;color:#222}
.terms-list li svg{position:absolute;left:-44px;top:0}
.sign-label{position:absolute;left:16px;font-family:'Fira Sans',sans-serif;font-weight:600;font-size:17px;color:var(--navy)}
.sign-line{position:absolute;height:0;border-top:1.5px solid #9a9a9a}
</style>
</head>
<body>

<section class="page page--estimate">
  <svg class="header-art" width="531" height="92" viewBox="0 0 531 92">
    <rect x="0" y="0" width="531" height="92" fill="var(--grey)"/>
    <polygon points="0,0 269,0 242,92 0,92" fill="#fff"/>
    <polygon points="0,0 265,0 241,81 0,81" fill="var(--navy)"/>
    <polygon points="0,81 241,81 238,92 0,92" fill="var(--orange)"/>
  </svg>
  <div class="brand brand--header">KEYSTONE PAVING</div>
  <div class="recipient">
    <strong>To: Daniel Marlowe</strong><br>
    418 5th Street NE Dover 34210<br>
    dmarlowe@mailbox.com
  </div>

  <div class="estimate-title">
    <h1>DANIEL MARLOWE</h1>
    <h2>New concrete pad</h2>
    <p>Bid#: 20-0182</p>
  </div>

  <table class="line-items">
    <colgroup><col style="width:236px"><col style="width:86px"><col style="width:48px"><col style="width:59px"><col style="width:72px"></colgroup>
    <thead>
      <tr><th>Item</th><th class="c">Quantity</th><th class="c">U/M</th><th class="c">Unit$</th><th class="c">Total $</th></tr>
    </thead>
    <tbody>
      <tr class="row-main">
        <td class="desc">Form, Pour &amp; Finish New Concrete Slab (24' x 24' x 4"). Includes:<br>3000psi Concrete Mix, Footer (12" x 8") with One (#5) Continuous Rebar, Wire Mesh Reinforcement and Saw-Cut Expansion Joints</td>
        <td class="num">576</td><td class="num">SF</td><td class="num">58.65</td><td class="money">$4,982.40</td>
      </tr>
      <tr class="row-opt">
        <td class="desc">OPTIONAL: Add (2' x 24' x 4") Small Ramp Area</td>
        <td class="num">48</td><td class="num">SF</td><td class="num">$8.65</td><td class="money">$415.20</td>
      </tr>
      <tr class="row-total">
        <td></td><td></td><td class="label" colspan="2">Total Price</td><td class="money">$5,397.60</td>
      </tr>
    </tbody>
  </table>

  <div class="brand brand--faint">KEYSTONE PAVING</div>
  <div class="foot-band"></div>
</section>

<section class="page page--terms">
  <svg class="header-art" width="531" height="33" viewBox="0 0 531 33">
    <rect x="0" y="0" width="531" height="33" fill="var(--grey)"/>
    <polygon points="0,0 270,0 244,33 0,33" fill="#fff"/>
    <polygon points="0,0 266,0 244,29 0,29" fill="var(--navy)"/>
    <polygon points="0,29 244,29 241,33 0,33" fill="var(--orange)"/>
  </svg>
  <h1 class="terms-title">TERMS AND CONDITIONS</h1>
  <div class="dotted" style="top:86px"></div>

  <ul class="terms-list">
    <li style="top:114px"><svg width="11" height="11" viewBox="0 0 12 12"><circle cx="6" cy="6" r="5" fill="none" stroke="var(--orange)" stroke-width="1.3" stroke-dasharray="24 6"/><path d="M3.5 6 L5.5 8 L10 3" fill="none" stroke="var(--orange)" stroke-width="1.4"/></svg>Prices as quoted in this estimate are valid for (60) days only</li>
    <li style="top:149px"><svg width="11" height="11" viewBox="0 0 12 12"><circle cx="6" cy="6" r="5" fill="none" stroke="var(--orange)" stroke-width="1.3" stroke-dasharray="24 6"/><path d="M3.5 6 L5.5 8 L10 3" fill="none" stroke="var(--orange)" stroke-width="1.4"/></svg>Payment in full, less any previously paid amounts, is due to the Contractor upon completion of the proposed scope of work</li>
    <li style="top:193px"><svg width="11" height="11" viewBox="0 0 12 12"><circle cx="6" cy="6" r="5" fill="none" stroke="var(--orange)" stroke-width="1.3" stroke-dasharray="24 6"/><path d="M3.5 6 L5.5 8 L10 3" fill="none" stroke="var(--orange)" stroke-width="1.4"/></svg>&nbsp;All change order requests must be communicated in writing to the Contractor by the Client or their authorized representative.</li>
    <li style="top:237px"><svg width="11" height="11" viewBox="0 0 12 12"><circle cx="6" cy="6" r="5" fill="none" stroke="var(--orange)" stroke-width="1.3" stroke-dasharray="24 6"/><path d="M3.5 6 L5.5 8 L10 3" fill="none" stroke="var(--orange)" stroke-width="1.4"/></svg>All measurements listed in this estimate are approximate and may vary slightly due to actual field conditions.</li>
    <li style="top:277px"><svg width="11" height="11" viewBox="0 0 12 12"><circle cx="6" cy="6" r="5" fill="none" stroke="var(--orange)" stroke-width="1.3" stroke-dasharray="24 6"/><path d="M3.5 6 L5.5 8 L10 3" fill="none" stroke="var(--orange)" stroke-width="1.4"/></svg>&nbsp;It is agreed by the Contractor and the Client that complications and costs arising from unforeseen conditions and handling of unsuitable materials are not included in this estimate</li>
    <li style="top:323px"><svg width="11" height="11" viewBox="0 0 12 12"><circle cx="6" cy="6" r="5" fill="none" stroke="var(--orange)" stroke-width="1.3" stroke-dasharray="24 6"/><path d="M3.5 6 L5.5 8 L10 3" fill="none" stroke="var(--orange)" stroke-width="1.4"/></svg>Unless specifically listed in this estimate, the following items and their costs are not included: Maintenance of Traffic, Concrete Material Pumping, Testing, Excavation, Grading and Fill Material, Permits and Fees, Surveying and As-builts, Irrigation Repair. Landscaping and Root Mitigation, De-watering, Private Locates and Accessibility.</li>
    <li style="top:398px"><svg width="11" height="11" viewBox="0 0 12 12"><circle cx="6" cy="6" r="5" fill="none" stroke="var(--orange)" stroke-width="1.3" stroke-dasharray="24 6"/><path d="M3.5 6 L5.5 8 L10 3" fill="none" stroke="var(--orange)" stroke-width="1.4"/></svg>Private utility locating services using radio detection devices and, when necessary, ground penetrating radar are offered by Keystone Paving to assist in finding private utilities that may not have been located by the public one call system. Keystone Paving will not be responsible for private utilities that have not been located nor for the failure of the above equipment to accurately detect existing utilities since the equipment is fallible and existing site conditions may preclude the ability of the equipment to detect an identifiable signal.</li>
  </ul>

  <div class="dotted" style="top:508px"></div>

  <div class="sign-label" style="top:574px">Client Signature</div>
  <div class="sign-line" style="left:16px;top:632px;width:223px"></div>
  <div class="sign-label" style="top:674px">Date</div>
  <div class="sign-line" style="left:67px;top:690px;width:172px"></div>

  <div class="brand brand--footer">KEYSTONE PAVING</div>
  <div class="foot-band"></div>
</section>

</body>
</html>
```